Derek Hollins Business card

Hey there, I’m hoping to have a business card designed. I’m in Real estate and just switched to a new Brokerage called: The Property Quarter

The back could just be the company name maybe or whatever looks good!

I’ve attached some logos of our company and some cards my buddy had done up.

On the card:
Derek Hollins
derekhollins@mailbox-demo.com
587-214-6093
derekhollins-demo.ca

Target Market(s)

Home buyers and sellers

Industry/Entity Type

Real Estate

Contact Information for Business Card

just looking for a cool and modern design with my picture on it. I like the idea of Black and red being used.

Requirements
Must have
• all the details provided. I'm open to anything. Just want a professional looking card.

```html
<!DOCTYPE html>
<html lang="en">
<head>
<meta charset="utf-8">
<title>Derek Hollins – Business Card</title>
<link rel="stylesheet" href="https://fonts.googleapis.com/css2?family=Lato:wght@400;700;900&display=swap">
<style>
  :root {
    --backdrop: #141414;
    --card: #1b1b1d;
    --card-shade: #0e0e0f;
    --red: #d8203f;
    --white: #f2f2f2;
    --muted: #cfcfcf;
    --steel: #8a8a8c;
  }
  * { box-sizing: border-box; margin: 0; padding: 0; }
  html, body {
    width: 1200px; height: 977px; overflow: hidden;
    background: var(--backdrop);
    font-family: "Lato", Arial, sans-serif;
  }
  .canvas {
    position: relative; width: 1200px; height: 977px;
    display: flex; flex-direction: column; align-items: center; justify-content: center; gap: 44px;
  }
  .card {
    position: relative; width: 700px; height: 400px;
    border-radius: 22px; overflow: hidden;
    background: radial-gradient(ellipse at 50% 40%, #232325 0%, var(--card) 45%, var(--card-shade) 100%);
    box-shadow: 0 5px 0 var(--red), 0 20px 40px rgba(0,0,0,.6);
  }

  /* back */
  .card-back {
    display: flex; align-items: center; justify-content: center;
    padding: 0 80px;
  }
  .brand-name {
    display: block; width: 100%;
    text-align: center;
    font-weight: 900; font-size: 50px; line-height: 1.1; letter-spacing: 2px;
    color: var(--red); text-transform: uppercase;
  }

  /* front */
  .portrait {
    position: absolute; right: 0; top: 0; width: 330px; height: 400px;
    background: linear-gradient(180deg, #2a2d33 0%, #1f2228 50%, #141518 100%);
  }
  .identity { position: absolute; left: 46px; top: 52px; }
  .identity-mark { display: flex; align-items: center; gap: 12px; }
  .identity-mark .square { width: 18px; height: 18px; background: var(--red); }
  .identity-mark .name { font-weight: 900; font-size: 32px; color: var(--white); text-transform: uppercase; letter-spacing: 1px; }
  .identity-sub {
    margin-top: 6px; padding-top: 6px; border-top: 1px solid var(--steel);
    font-size: 11px; letter-spacing: 2px; color: var(--muted); text-transform: uppercase;
  }
  .title-block { position: absolute; left: 46px; top: 180px; }
  .person { font-weight: 900; font-size: 30px; color: var(--red); text-transform: uppercase; line-height: 1; }
  .role { font-size: 18px; color: var(--white); text-transform: uppercase; margin-top: 4px; }
  .contacts { position: absolute; left: 46px; top: 268px; list-style: none; }
  .contacts li { display: flex; align-items: center; gap: 12px; color: var(--white); font-size: 17px; margin-bottom: 10px; }
  .contacts svg { width: 16px; height: 16px; fill: var(--red); flex: none; }
</style>
</head>
<body>
<main class="canvas">
  <section class="card card-back">
    <span class="brand-name">The Property Quarter</span>
  </section>

  <section class="card card-front">
    <div class="portrait" role="img" aria-label="Portrait photo of Derek Hollins in a dark suit and white shirt"></div>

    <div class="identity">
      <div class="identity-mark">
        <span class="square"></span>
        <span class="name">Derek Hollins</span>
      </div>
      <div class="identity-sub">The Property Quarter</div>
    </div>

    <div class="title-block">
      <div class="person">Derek Hollins</div>
      <div class="role">Realtor</div>
    </div>

    <ul class="contacts">
      <li>
        <svg viewBox="0 0 24 24" aria-hidden="true"><path d="M6.6 10.8a15.1 15.1 0 0 0 6.6 6.6l2.2-2.2c.3-.3.7-.4 1-.2 1.1.4 2.3.6 3.6.6.6 0 1 .4 1 1V20c0 .6-.4 1-1 1A17 17 0 0 1 3 4c0-.6.4-1 1-1h3.5c.6 0 1 .4 1 1 0 1.3.2 2.5.6 3.6.1.3 0 .7-.2 1z"/></svg>
        587-214-6093
      </li>
      <li>
        <svg viewBox="0 0 24 24" aria-hidden="true"><path d="M2 5h20v14H2z M4 7v.5l8 5 8-5V7l-8 5z" fill-rule="evenodd"/></svg>
        derekhollins@mailbox-demo.com
      </li>
      <li>
        <svg viewBox="0 0 24 24" aria-hidden="true"><path d="M12 2a10 10 0 1 0 0 20 10 10 0 0 0 0-20zm0 2c1.3 1.6 2.1 3.7 2.3 7H9.7c.2-3.3 1-5.4 2.3-7zm-4.3 7H4.1a8 8 0 0 1 4.8-6.4c-.8 1.7-1.1 3.9-1.2 6.4zm0 2c.1 2.5.4 4.7 1.2 6.4A8 8 0 0 1 4.1 13zm2 0h4.6c-.2 3.3-1 5.4-2.3 7-1.3-1.6-2.1-3.7-2.3-7zm6.6 0h3.6a8 8 0 0 1-4.8 6.4c.8-1.7 1.1-3.9 1.2-6.4zm0-2c-.1-2.5-.4-4.7-1.2-6.4a8 8 0 0 1 4.8 6.4z"/></svg>
        derekhollins-demo.ca
      </li>
    </ul>
  </section>
</main>
</body>
</html>
```